Eiskarte für Landhotel
Zielgruppe
Landhotel und Restaurant, Sommergarten, Biergarten
Aufgabenstellung
Eiskarte:
Ländlich, Bäuerlich, Vintage, gepflegte Küche

```html
<!DOCTYPE html>
<html lang="de">
<head>
<meta charset="utf-8">
<title>Eiskarte – Landhotel Selma</title>
<link rel="stylesheet" href="https://fonts.googleapis.com/css2?family=Josefin+Sans:wght@400&family=Lobster&display=swap">
<style>
  :root {
    --paper: #e3cdc4;
    --stripe-rose: #d2ada1;
    --stripe-grey: #b8bbbe;
    --frame-grey: #8a8f93;
    --brick: #a64b3f;
    --cream: #f3ebe7;
    --ice-light: #dcd8d8;
    --ice-mid: #b9b4b5;
  }
  * { box-sizing: border-box; margin: 0; padding: 0; }
  html, body { width: 848px; height: 1200px; overflow: hidden; background: var(--paper); }
  .menu-cover { position: relative; width: 848px; height: 1200px; background: var(--paper); }
  .frame-art { position: absolute; inset: 0; }
  .brand-name {
    position: absolute; left: 0; right: 0; top: 258px;
    text-align: center;
    font-family: "Josefin Sans", sans-serif; font-weight: 400;
    font-size: 52px; letter-spacing: 4px; line-height: 1;
    color: var(--brick);
  }
  .menu-title {
    position: absolute; left: 0; right: 0; top: 470px; text-align: center;
    font-family: "Lobster", cursive; font-size: 158px; font-weight: 400; color: var(--brick);
    transform: rotate(-5deg);
    text-shadow:
      6px 0 0 var(--cream), -6px 0 0 var(--cream), 0 6px 0 var(--cream), 0 -6px 0 var(--cream),
      5px 5px 0 var(--cream), -5px 5px 0 var(--cream), 5px -5px 0 var(--cream), -5px -5px 0 var(--cream),
      11px 0 0 var(--frame-grey), -11px 0 0 var(--frame-grey), 0 11px 0 var(--frame-grey), 0 -11px 0 var(--frame-grey),
      8px 8px 0 var(--frame-grey), -8px 8px 0 var(--frame-grey), 8px -8px 0 var(--frame-grey), -8px -8px 0 var(--frame-grey);
  }
  .sundae-art {
    position: absolute; left: 316px; top: 712px; width: 300px; height: 345px;
    border-radius: 46% 46% 30% 30% / 40% 40% 20% 20%;
    background: radial-gradient(ellipse at 45% 30%, var(--ice-light), var(--ice-mid) 60%, rgba(184,187,190,0) 100%);
  }
  .corner-ornament {
    position: absolute; width: 84px; height: 84px; border-radius: 40%;
    background: radial-gradient(circle, var(--stripe-grey), rgba(184,187,190,0) 75%);
  }
  .corner-ornament.top-left { left: 32px; top: 60px; }
  .corner-ornament.top-right { right: 32px; top: 60px; }
  .corner-ornament.bottom-left { left: 32px; bottom: 60px; }
  .corner-ornament.bottom-right { right: 32px; bottom: 60px; }
</style>
</head>
<body>
<main class="menu-cover">
  <svg class="frame-art" width="848" height="1200" viewBox="0 0 848 1200" aria-hidden="true">
    <g class="awning">
      <path fill="var(--stripe-rose)" d="M54 88h82v306a41 41 0 0 1-82 0z"/>
      <path fill="var(--stripe-grey)" d="M136 88h82v306a41 41 0 0 1-82 0z"/>
      <path fill="var(--stripe-rose)" d="M218 88h82v306a41 41 0 0 1-82 0z"/>
      <path fill="var(--stripe-grey)" d="M300 88h82v306a41 41 0 0 1-82 0z"/>
      <path fill="var(--stripe-rose)" d="M382 88h82v306a41 41 0 0 1-82 0z"/>
      <path fill="var(--stripe-grey)" d="M464 88h82v306a41 41 0 0 1-82 0z"/>
      <path fill="var(--stripe-rose)" d="M546 88h82v306a41 41 0 0 1-82 0z"/>
      <path fill="var(--stripe-grey)" d="M628 88h82v306a41 41 0 0 1-82 0z"/>
      <path fill="var(--stripe-rose)" d="M710 88h82v306a41 41 0 0 1-82 0z"/>
    </g>
    <g class="frame-lines" stroke="var(--frame-grey)" fill="none">
      <line x1="150" y1="67" x2="698" y2="67" stroke-width="2"/>
      <line x1="150" y1="75" x2="698" y2="75" stroke-width="1"/>
      <line x1="150" y1="1125" x2="698" y2="1125" stroke-width="1"/>
      <line x1="150" y1="1133" x2="698" y2="1133" stroke-width="2"/>
      <line x1="31" y1="150" x2="31" y2="1050" stroke-width="2"/>
      <line x1="43" y1="150" x2="43" y2="1050" stroke-width="1"/>
      <line x1="817" y1="150" x2="817" y2="1050" stroke-width="2"/>
      <line x1="805" y1="150" x2="805" y2="1050" stroke-width="1"/>
    </g>
  </svg>

  <div class="corner-ornament top-left" role="img" aria-label="Blattornament in der Ecke"></div>
  <div class="corner-ornament top-right" role="img" aria-label="Blattornament in der Ecke"></div>
  <div class="corner-ornament bottom-left" role="img" aria-label="Blattornament in der Ecke"></div>
  <div class="corner-ornament bottom-right" role="img" aria-label="Blattornament in der Ecke"></div>

  <p class="brand-name">Landhotel Selma</p>

  <h1 class="menu-title">Eiskarte</h1>

  <div class="sundae-art" role="img" aria-label="Eisbecher mit drei Kugeln auf silbernem Fuß mit Löffel"></div>
</main>
</body>
</html>
```